Webdesign für führende Dienstleistungs- und Handelsplattform der Getränkebranche
Zielgruppe
Kornfeld Trank ist die führende Dienstleistungs- und Handelsplattform der Getränkebranche in Deutschland. Unsere Vision ist es, sowohl eine kanalübergreifende Plattform zu schaffen, die Einkauf, Vermarktung, Distribution und Service vereint, als auch in den spezifischen Geschäftsfeldern maßgeschneiderte Lösungen anzubieten. Die neue Website soll diese duale Ausrichtung klar kommunizieren: die Stärke der Dachmarke „Kornfeld Trank“ und die problemorientierte Kompetenz der einzelnen Geschäftsfelder.
Aufgabenstellung
Ziele der neuen Website:
1. Stärkung der Dachmarke „Kornfeld Trank“:
Die Website soll die Dachmarke klar positionieren, ihre Werte und ihren Impact auf die Getränkewirtschaft kommunizieren. Gleichzeitig soll deutlich werden, welche zentrale Rolle die Dachmarke als Plattform und Netzwerk für Synergien zwischen den Geschäftsfeldern einnimmt.
2. Klarheit und Fokussierung für Geschäftsfelder:
Die Seite soll die individuellen Leistungen der Geschäftsfelder klar hervorheben und potenziellen Kunden direkt ansprechende, problemorientierte Lösungen bieten. Jedes Geschäftsfeld soll als eigenständige, klar positionierte Einheit erkennbar sein, aber gleichzeitig die Verbindung zur Dachmarke beibehalten.
3. Nutzerzentrierte Kommunikation:
Besucher sollen schnell und intuitiv verstehen, welche Lösungen für ihre spezifischen Bedürfnisse geboten werden. Die Website sollte klar strukturierte Einstiegswege bieten, die sich an den Kernproblemen der Zielgruppen orientieren.
4. Synergien und Netzwerk betonen:
Es soll vermittelt werden, dass Kunden, die mehrere Leistungen der Kornfeld Trank nutzen, von einzigartigen Synergien und einem umfassenden Netzwerk profitieren.
5. Praxisnähe und Storytelling:
Die Website soll die Leistungen nicht abstrakt darstellen, sondern praxisnahe Erfolgsgeschichten erzählen, die Kundenbedürfnisse aufgreifen und emotionale Verbindungen schaffen.
Design- und Struktur-Anforderungen:
1. Modulare Struktur:
o Die Hauptseite soll die Werte und Leistungen der Dachmarke kommunizieren.
o Subseiten für Geschäftsfelder sollen sich in Farbgebung und Struktur leicht unterscheiden, um ihre Eigenständigkeit zu unterstreichen.
o Die Struktur muss klar und nutzerfreundlich sein, ohne die Komplexität der Organisation zu betonen.
2. Hero Images und emotionale Ansprache:
o Startseite und Geschäftsfelder sollen durch großformatige, ästhetische Bilder in Kombi..

```html
<!DOCTYPE html>
<html lang="de">
<head>
<meta charset="utf-8">
<title>Kornfeld Trank – Webdesign</title>
<link href="https://fonts.googleapis.com/css2?family=Archivo:wght@400;600;800&family=Inter:wght@400;600&display=swap" rel="stylesheet">
<style>
:root{
  --stage:#e9e9ec;
  --dark:#111112;
  --white:#ffffff;
  --ink:#151517;
  --muted:#8a8a90;
  --blue:#1f5bd8;
  --cyan:#38c6f4;
  --faint-dark:#2c2c30;
  --faint-light:#e4e4e8;
}
*{box-sizing:border-box;margin:0;padding:0}
html,body{width:686px;height:1200px;overflow:hidden}
body{background:var(--stage);font-family:"Inter",sans-serif;position:relative}
.page{position:absolute;top:22px;overflow:hidden;box-shadow:0 4px 14px rgba(0,0,0,.12)}
.page--home{left:40px;width:270px;height:1090px;background:var(--dark);color:var(--white)}
.page--trade{left:336px;width:294px;height:950px;background:var(--white);color:var(--ink)}
.abs{position:absolute}
.photo{position:absolute;border-radius:2px}
.nav{position:absolute;top:8px;left:12px;right:12px;display:flex;justify-content:space-between;align-items:center}
.nav__brand{font-family:"Archivo",sans-serif;font-weight:800;font-size:6px;letter-spacing:.3px}
.nav__links{display:flex;gap:5px}
.nav__links span{width:14px;height:3px;background:currentColor;opacity:.6;border-radius:1px}
.nav__cta{width:22px;height:7px;border-radius:4px;background:var(--cyan)}
.brand-word{font-family:"Archivo",sans-serif;font-weight:800;line-height:.95;text-transform:uppercase}
.body-text{font-size:6.2px;line-height:1.5}
.page--home .body-text{color:#d6d6da}
.page--trade .body-text{color:#3b3b40}
.heading{font-family:"Archivo",sans-serif;font-weight:600;font-size:11px;line-height:1.15}
.btn{display:inline-block;font-size:5px;padding:2px 7px;border-radius:6px;background:var(--cyan);color:var(--ink);font-weight:600}
.caption{position:absolute;left:0;right:0;text-align:center;font-family:"Archivo",sans-serif;font-size:11px;line-height:1.2}
.network{position:absolute;width:150px;height:130px;border-radius:50%}
.page--home .network{background:radial-gradient(circle,#26262b 0%,#1a1a1d 55%,rgba(17,17,18,0) 72%)}
.page--trade .network{background:radial-gradient(circle,#f1f1f4 0%,#f6f6f8 55%,rgba(255,255,255,0) 72%)}
.ghost-word{position:absolute;left:0;right:0;text-align:center;font-family:"Archivo",sans-serif;font-weight:800;font-size:30px;letter-spacing:-.5px;white-space:nowrap}
.page--home .ghost-word{color:var(--faint-dark)}
.page--trade .ghost-word{color:var(--faint-light)}
.badge{position:absolute;width:46px;height:46px;border-radius:50%;background:var(--blue);display:flex;align-items:center;justify-content:center;text-align:center;font-family:"Archivo",sans-serif;font-weight:800;font-size:6px;line-height:1;color:var(--white);text-transform:uppercase}
.card-title{font-size:6px;font-weight:600;line-height:1.3}
.footer-col{font-size:4.8px;line-height:1.8}
.footer-col b{display:block;font-weight:600}
.rule{position:absolute;left:12px;right:12px;height:1px}
</style>
</head>
<body>

<main class="page page--home">
  <div class="photo" style="left:0;top:0;width:270px;height:240px;background:linear-gradient(160deg,#6b4a3a,#2a1d18 55%,#4d3526)" role="img" aria-label="Gäste stoßen mit Weingläsern an"></div>
  <nav class="nav"><span class="nav__brand">KORNFELD TRANK</span><span class="nav__links"><span></span><span></span><span></span></span><span class="nav__cta"></span></nav>
  <div class="brand-word abs" style="left:12px;top:196px;font-size:16px">Kornfeld<br>Trank</div>

  <p class="body-text abs" style="left:12px;top:256px;width:240px">Unser Team rund um die Getränkebranche verbindet Einkauf, Vermarktung, Logistik und Service auf einer gemeinsamen Plattform. Wir begleiten Gastronomie, Handel und Hersteller mit Erfahrung, Netzwerk und Lösungen, die im Alltag funktionieren. So entstehen Synergien, von denen jeder Partner spürbar profitiert – heute und in Zukunft.</p>

  <div class="photo" style="left:12px;top:360px;width:90px;height:62px;background:linear-gradient(135deg,#7a5a3c,#3b2a1e)" role="img" aria-label="Gedeckter Restauranttisch"></div>
  <h2 class="heading abs" style="left:112px;top:362px;width:140px">Restaurants und Hotellerie</h2>
  <p class="body-text abs" style="left:112px;top:380px;width:140px">Sortiment, Beratung und Belieferung aus einer Hand.</p>
  <span class="btn abs" style="left:112px;top:410px">Mehr erfahren</span>

  <div class="photo" style="left:12px;top:432px;width:78px;height:40px;background:linear-gradient(135deg,#5b6470,#2c3036)" role="img" aria-label="Getränkeregal im Markt"></div>
  <div class="photo" style="left:96px;top:432px;width:78px;height:40px;background:linear-gradient(135deg,#8a6a44,#3e2f22)" role="img" aria-label="Barkeeper an der Theke"></div>
  <div class="photo" style="left:180px;top:432px;width:78px;height:40px;background:linear-gradient(135deg,#4a5a48,#252b24)" role="img" aria-label="Flaschen im Kühlregal"></div>

  <div class="photo" style="left:12px;top:482px;width:90px;height:80px;background:linear-gradient(135deg,#3c4a5c,#1e242c)" role="img" aria-label="Lagerhalle mit Paletten"></div>
  <div class="abs" style="left:112px;top:482px;width:90px;height:36px;background:var(--blue);padding:5px">
    <div class="card-title">Logistik &amp; Service</div>
    <div style="font-size:4.8px;line-height:1.4;color:#dfe7ff">Schnell, zuverlässig, bundesweit.</div>
  </div>
  <div class="photo" style="left:112px;top:524px;width:146px;height:38px;background:linear-gradient(135deg,#6f7680,#3a3f46)" role="img" aria-label="Lieferfahrzeug vor dem Lager"></div>
  <div class="brand-word abs" style="left:150px;top:538px;font-size:10px">Kornfeld Trank</div>

  <div class="network" style="left:60px;top:584px" role="img" aria-label="Netzwerk der Geschäftsfelder rund um die Dachmarke"></div>
  <div class="ghost-word" style="top:634px">KORNFELD TRANK</div>
  <div class="badge" style="left:112px;top:626px">Kornfeld<br>Trank</div>
  <p class="caption" style="top:734px">Die Kornfeld Trank Einheit.<br>Für jeden Schritt<br>die richtige Lösung</p>

  <h2 class="heading abs" style="left:12px;top:796px;width:115px">Kornfeld Trank für Getränkefachhandel</h2>
  <p class="body-text abs" style="left:12px;top:826px;width:115px">Sortimentsberatung, Marketing und Einkauf für den Fachhandel.</p>
  <span class="btn abs" style="left:12px;top:854px">Mehr erfahren</span>
  <div class="photo" style="left:135px;top:792px;width:123px;height:66px;background:linear-gradient(135deg,#5a4c3e,#2a221b)" role="img" aria-label="Getränkemarkt mit Kunden"></div>

  <h2 class="heading abs" style="left:0;right:0;top:884px;text-align:center;font-size:10px">Aktuelles aus unserer Branche</h2>
  <div class="photo" style="left:12px;top:904px;width:78px;height:46px;background:linear-gradient(135deg,#8b6b4a,#3f3024)" role="img" aria-label="Weinverkostung"></div>
  <div class="photo" style="left:96px;top:904px;width:78px;height:46px;background:linear-gradient(135deg,#6a7a60,#2f362a)" role="img" aria-label="Team bei einer Besprechung"></div>
  <div class="photo" style="left:180px;top:904px;width:78px;height:46px;background:linear-gradient(135deg,#7a5a62,#35262a)" role="img" aria-label="Messestand der Branche"></div>
  <p class="card-title abs" style="left:12px;top:956px;width:78px">Neue Partner im Fachhandel</p>
  <p class="card-title abs" style="left:96px;top:956px;width:78px">Trends der Saison im Überblick</p>
  <p class="card-title abs" style="left:180px;top:956px;width:78px">Rückblick auf die Fachmesse</p>

  <div class="brand-word abs" style="left:12px;top:1012px;font-size:11px">Kornfeld<br>Trank</div>
  <div class="footer-col abs" style="left:120px;top:1010px;color:#bdbdc2"><b>Unternehmen</b>Über uns<br>Karriere<br>Presse</div>
  <div class="footer-col abs" style="left:165px;top:1010px;color:#bdbdc2"><b>Leistungen</b>Großhandel<br>Fachhandel<br>Gastronomie</div>
  <div class="footer-col abs" style="left:215px;top:1010px;color:#bdbdc2"><b>Kontakt</b>Anfrage<br>Standorte<br>Service</div>
  <div class="rule" style="top:1066px;background:#333338"></div>
  <p class="abs" style="left:12px;top:1072px;font-size:4.5px;color:var(--muted)">© Kornfeld Trank · Impressum · Datenschutz</p>
</main>

<main class="page page--trade">
  <div class="photo" style="left:0;top:0;width:294px;height:150px;background:linear-gradient(160deg,#5c7896,#243548 60%,#3b5068)" role="img" aria-label="Hochregallager mit Getränkepaletten"></div>
  <nav class="nav" style="color:var(--white)"><span class="nav__brand">KORNFELD TRANK</span><span class="nav__links"><span></span><span></span><span></span></span><span class="nav__cta"></span></nav>
  <svg class="abs" style="left:14px;top:100px" width="18" height="18" viewBox="0 0 18 18" aria-hidden="true"><rect width="18" height="18" fill="var(--blue)"/><path d="M5 5l4 4-4 4M9 5l4 4-4 4" fill="none" stroke="#fff" stroke-width="1.6"/></svg>
  <h1 class="brand-word abs" style="left:38px;top:99px;font-size:21px;color:var(--white)">Großhandel</h1>

  <p class="body-text abs" style="left:14px;top:166px;width:266px">Der partnerschaftliche Großhandel unter dem Dach von Kornfeld Trank ist eine starke Einheit für die Getränkebranche. Mit bundesweiter Logistik, breitem Sortiment und persönlicher Betreuung sorgen wir dafür, dass unsere Partner jederzeit lieferfähig bleiben und sich auf ihr Geschäft konzentrieren können.</p>

  <div class="photo" style="left:14px;top:244px;width:84px;height:90px;background:linear-gradient(135deg,#6d7480,#343840)" role="img" aria-label="Mitarbeiter im Lager"></div>
  <div class="abs" style="left:105px;top:244px;width:84px;height:90px;background:var(--blue);color:var(--white);padding:6px">
    <div class="card-title">Sortiment &amp; Logistik</div>
    <div style="font-size:4.8px;line-height:1.45;color:#dfe7ff;margin-top:3px">Alles aus einer Hand – vom Einkauf bis zur Zustellung.</div>
  </div>
  <div class="photo" style="left:196px;top:244px;width:84px;height:90px;background:linear-gradient(135deg,#8a7a5e,#3d3528)" role="img" aria-label="Getränkekisten im Regal"></div>
  <p class="body-text abs" style="left:14px;top:342px;width:266px">Mit festen Ansprechpartnern, klaren Prozessen und digitalen Bestellwegen wird der Großhandel zum verlässlichen Partner.</p>

  <h2 class="heading abs" style="left:14px;top:410px;font-weight:400">Wie wir <b>Arbeiten</b></h2>
  <p class="body-text abs" style="left:14px;top:430px;width:140px">Persönlich, planbar und nah am Kunden – mit Teams in allen Regionen.</p>
  <div class="photo" style="left:170px;top:400px;width:110px;height:70px;background:linear-gradient(135deg,#4e5a6a,#232a33)" role="img" aria-label="Mitarbeiter mit Tablet im Lager"></div>

  <h2 class="heading abs" style="left:14px;top:504px;font-weight:400">Ihr <b>Nutzen</b></h2>
  <p class="body-text abs" style="left:14px;top:524px;width:140px">Weniger Aufwand, mehr Auswahl und starke Konditionen für Ihr Geschäft.</p>
  <div class="photo" style="left:170px;top:494px;width:110px;height:66px;background:linear-gradient(135deg,#7a6650,#352c22)" role="img" aria-label="Getränkepaletten an der Rampe"></div>

  <div class="network" style="left:72px;top:592px" role="img" aria-label="Netzwerk der Geschäftsfelder rund um die Dachmarke"></div>
  <div class="ghost-word" style="top:642px">KORNFELD TRANK</div>
  <div class="badge" style="left:124px;top:634px">Kornfeld<br>Trank</div>
  <p class="caption" style="top:744px">Die Kornfeld Trank Einheit.<br>Für jeden Schritt<br>die richtige Lösung</p>

  <div class="brand-word abs" style="left:14px;top:842px;font-size:11px">Kornfeld<br>Trank</div>
  <div class="footer-col abs" style="left:14px;top:874px;color:#55555b">Musterweg 12 · 10115 Berlin</div>
  <div class="footer-col abs" style="left:140px;top:842px;color:#55555b"><b>Leistungen</b>Großhandel<br>Fachhandel<br>Gastronomie</div>
  <div class="footer-col abs" style="left:200px;top:842px;color:#55555b"><b>Kontakt</b>Anfrage<br>Standorte<br>Service</div>
  <span class="btn abs" style="left:246px;top:908px">Kontakt</span>
  <div class="rule" style="top:926px;left:14px;right:14px;background:#e2e2e6"></div>
  <p class="abs" style="left:14px;top:932px;font-size:4.5px;color:var(--muted)">© Kornfeld Trank · Impressum · Datenschutz</p>
</main>

</body>
</html>
```